Modern Design Business Card industrial maintenance company

Business card design for Company named Brookvale Equipment Services

Target Market(s)

Industrial

Industry/Entity Type

Maintenance and repair

Contact Information for Business Card

Place holder for address, office phone, mobile number and email

Requirements
Must have
• Clean modern look
Nice to have
• N/a

```html
<!DOCTYPE html>
<html lang="en">
<head>
<meta charset="utf-8">
<title>Brookvale Equipment Services – Business Card</title>
<link href="https://fonts.googleapis.com/css2?family=Open+Sans:wght@400;600;700&display=swap" rel="stylesheet">
<style>
  :root {
    --stage: #e4e2df;
    --card: #0b0b0b;
    --card-edge: #1a1a1a;
    --ink: #ffffff;
    --ink-soft: #d9d9d9;
    --pattern-a: #141414;
    --pattern-b: #202020;
  }
  * { margin: 0; padding: 0; box-sizing: border-box; }
  html, body {
    width: 1200px; height: 1017px; overflow: hidden;
    background: var(--stage);
    font-family: "Open Sans", Arial, sans-serif;
  }
  .sheet {
    width: 1200px; height: 1017px;
    display: flex; flex-direction: column; align-items: center; justify-content: center;
    gap: 40px;
  }
  .card {
    position: relative;
    width: 800px; height: 457px;
    background: var(--card);
    color: var(--ink);
    overflow: hidden;
    box-shadow: 0 10px 30px rgba(0,0,0,.25);
  }

  /* Front */
  .company {
    position: absolute; left: 62px; top: 52px;
    font-weight: 600; text-transform: uppercase; color: var(--ink);
    line-height: 1.15;
  }
  .company .line-1 { display: block; font-size: 40px; letter-spacing: 5px; }
  .company .line-2 { display: block; font-size: 13px; letter-spacing: 7.4px; }
  .person { position: absolute; left: 62px; top: 152px; }
  .person .name { font-size: 25px; font-weight: 700; }
  .person .role { font-size: 17px; font-weight: 400; color: var(--ink-soft); margin-top: 2px; }
  .address {
    position: absolute; left: 62px; top: 242px;
    font-size: 15px; line-height: 1.65; color: var(--ink-soft);
  }
  .contacts {
    position: absolute; left: 62px; top: 312px;
    list-style: none; font-size: 18px;
  }
  .contacts li { display: flex; align-items: center; gap: 18px; height: 27px; }
  .contacts svg { width: 16px; height: 16px; fill: none; stroke: var(--ink); stroke-width: 1.6; flex: none; }

  .brand-mark {
    position: absolute; right: 60px; top: 84px;
    width: 290px; height: 290px;
    display: flex; align-items: center; justify-content: center;
  }
  .brand-mark .ring {
    position: absolute; inset: 0;
    border: 10px solid var(--ink); border-radius: 50%;
  }
  .brand-mark .brand-name {
    font-size: 30px; font-weight: 600; text-transform: uppercase; letter-spacing: 2px;
  }

  /* Back */
  .pattern-field {
    position: absolute; inset: 0;
    background: radial-gradient(ellipse at center, var(--pattern-b) 0%, var(--pattern-a) 70%, var(--card) 100%);
  }
  .back-brand {
    position: absolute; inset: 0;
    display: flex; align-items: center; justify-content: center; gap: 22px;
  }
  .back-brand .dot {
    width: 64px; height: 64px; border: 5px solid var(--ink); border-radius: 50%;
  }
  .back-brand .brand-name {
    font-weight: 600; text-transform: uppercase; line-height: 1.15;
  }
  .back-brand .brand-name span:first-child { display: block; font-size: 34px; letter-spacing: 4px; }
  .back-brand .brand-name span:last-child { display: block; font-size: 11.5px; letter-spacing: 6.2px; }
</style>
</head>
<body>
<main class="sheet">
  <section class="card card-front">
    <div class="company"><span class="line-1">Brookvale</span><span class="line-2">Equipment Services</span></div>
    <div class="person">
      <p class="name">Your Name Here</p>
      <p class="role">Managing Director</p>
    </div>
    <p class="address">418 N. Harlow Crest,<br>#210 Fairview, Oregon 97024</p>
    <ul class="contacts">
      <li><svg viewBox="0 0 16 16"><path d="M3 1.5l3 .5 1 3-2 1.5a9 9 0 0 0 4.5 4.5L11 9l3 1 .5 3-2 1.5C7 14 2 9 1.5 3.5z"/></svg>(503) 555-0147</li>
      <li><svg viewBox="0 0 16 16"><rect x="4" y="1" width="8" height="14" rx="1.5"/><line x1="7" y1="12.5" x2="9" y2="12.5"/></svg>(503) 555-0147</li>
      <li><svg viewBox="0 0 16 16"><rect x="1" y="3" width="14" height="10"/><path d="M1 3l7 6 7-6"/></svg>youremail@youremail.com</li>
      <li><svg viewBox="0 0 16 16"><circle cx="8" cy="8" r="6.5"/><ellipse cx="8" cy="8" rx="3" ry="6.5"/><line x1="1.5" y1="8" x2="14.5" y2="8"/></svg>www.yourwebsite.com</li>
    </ul>
    <div class="brand-mark">
      <div class="ring"></div>
      <span class="brand-name">Brookvale</span>
    </div>
  </section>

  <section class="card card-back">
    <div class="pattern-field" role="img" aria-label="Faint repeating brand pattern across the card back"></div>
    <div class="back-brand">
      <div class="dot"></div>
      <p class="brand-name"><span>Brookvale</span><span>Equipment Services</span></p>
    </div>
  </section>
</main>
</body>
</html>
```